QRMT - Immigration and Business Consulting Marketing Brochure

81/2 x 11 tri-fold brochure or 11 x 17 tri-fold brochure which ever is suitable to display all our content. Full-colour 4/4,
Immigration and Business Consulting
Present services we provide and web-sites associated with our business. 1st page needs a picture of something related to the first step (choice of picture for your option). Logo would also need to be on this page and contact information page (Logo is uploaded) Uploaded file has all information that we would desire in our brochure. Each section is labeled for your convenience.

Please visit our primary website if you need further information - www.qrmt.ca

Target Market(s)

B2B Employers needing Recruitment/Immigration assistance and foreign clients looking to immigrate to Canada.

Industry/Entity Type

Business

Font styles to use
Serif

Requirements
Must have
• Company Logo
Nice to have
• Pictures for specific areas and sections of brochure
Should not have
• Profanity/sexual explicit photos

```html
<!DOCTYPE html>
<html lang="en">
<head>
<meta charset="utf-8">
<title>QRMT Tri-fold Brochure</title>
<link href="https://fonts.googleapis.com/css2?family=Open+Sans:wght@400;600&family=Questrial&family=Kalam:wght@400&display=swap" rel="stylesheet">
<style>
  :root {
    --page-bg: #ece7df;
    --paper: #ffffff;
    --navy: #355f8f;
    --navy-dark: #2d5281;
    --ink: #333333;
    --list-blue: #2f5a8c;
    --accent: #e8731f;
    --photo-light: #cfe3ef;
    --photo-mid: #7fb0cf;
    --people-light: #f2f3f5;
    --people-mid: #a9b4c2;
  }
  * { box-sizing: border-box; margin: 0; padding: 0; }
  html, body { width: 1200px; height: 950px; overflow: hidden; }
  body { background: var(--page-bg); font-family: "Open Sans", sans-serif; color: var(--ink); }

  .brochure {
    position: absolute; left: 30px; top: 35px;
    width: 1140px; height: 880px;
    display: flex;
    box-shadow: 0 6px 16px rgba(0,0,0,.25);
  }
  .panel { position: relative; height: 100%; }

  /* Left: introduction */
  .panel-intro { width: 371px; background: var(--paper); }
  .intro-photo {
    height: 300px;
    background: linear-gradient(160deg, var(--photo-mid) 0%, var(--photo-light) 55%, var(--paper) 100%);
  }
  .intro-body { padding: 22px 22px 0 43px; }
  .intro-title {
    font-family: "Questrial", sans-serif; font-weight: 400;
    font-size: 25px; color: var(--ink); margin-bottom: 16px; letter-spacing: .2px;
  }
  .intro-text { font-size: 13.2px; line-height: 17.2px; text-align: justify; margin-bottom: 6px; }
  .service-list { list-style: none; margin-top: 16px; }
  .service-list li {
    position: relative; padding-left: 25px;
    font-size: 14px; font-weight: 600; color: var(--list-blue);
    line-height: 17.5px; margin-bottom: 6.8px;
  }
  .service-list li.wrap { padding-left: 16px; }
  .service-list li svg { position: absolute; left: 0; top: 4px; }

  /* Middle: contact */
  .panel-contact { width: 385px; background: var(--navy); color: #fff; }
  .map-area {
    position: absolute; left: 0; top: 220px; width: 385px; height: 360px;
    background: radial-gradient(ellipse at 50% 45%, rgba(255,255,255,.06), rgba(255,255,255,0) 70%);
  }
  .brand { position: absolute; left: 0; right: 0; text-align: center; font-family: "Questrial", sans-serif; }
  .brand-contact { top: 88px; font-size: 58px; color: #fff; letter-spacing: 2px; }
  .brand-mark {
    display: block; margin: 0 auto 6px; width: 36px; height: 36px; border-radius: 50%;
  }
  .brand-contact .brand-mark { background: #fff; }
  .sites {
    position: absolute; top: 560px; left: 0; right: 0; text-align: center;
    font-family: "Questrial", sans-serif; font-size: 17.5px; font-weight: 400;
    letter-spacing: 2.2px; line-height: 23.5px;
  }
  .contact-list { position: absolute; top: 686px; left: 78px; list-style: none;
    font-family: "Questrial", sans-serif; font-size: 17.5px; letter-spacing: 1px; line-height: 25px; }
  .contact-list li { position: relative; padding-left: 34px; }
  .contact-list svg { position: absolute; left: 0; top: 4px; }

  /* Right: cover */
  .panel-cover { width: 384px; background: var(--paper); }
  .brand-cover { top: 90px; font-size: 58px; color: var(--navy-dark); letter-spacing: 2px; }
  .brand-cover .brand-mark { background: var(--navy-dark); }
  .cover-photo {
    position: absolute; top: 198px; left: 0; width: 384px; height: 455px;
    background: linear-gradient(180deg, var(--people-light) 0%, var(--people-mid) 45%, var(--people-light) 100%);
  }
  .tagline {
    position: absolute; top: 688px; left: 0; right: 0; text-align: center;
    font-family: "Questrial", sans-serif; font-size: 20px; line-height: 24.5px; color: var(--navy-dark);
  }
  .slogan {
    position: absolute; top: 772px; left: 0; right: 0; text-align: center;
    font-family: "Kalam", cursive; font-size: 25px; color: var(--accent);
  }
  .cover-url {
    position: absolute; top: 824px; left: 0; right: 0; text-align: center;
    font-family: "Questrial", sans-serif; font-size: 17px; letter-spacing: 1px; color: var(--ink);
  }
</style>
</head>
<body>
<main class="brochure">

  <section class="panel panel-intro">
    <div class="intro-photo" role="img" aria-label="Photo of a hand touching a tablet with a glowing world network of people"></div>
    <div class="intro-body">
      <h2 class="intro-title">QRMT INTRODUCTION</h2>
      <p class="intro-text">QRMT is an immigration and business consulting firm. QRMT specializes in providing growth, recruitment locally and abroad, relocation and retention strategies for growing businesses requiring workers.</p>
      <p class="intro-text">QRMT also provides consulting services for all types of Federal immigration applications and Provincial Nominee Program applications through a streamlined approach.</p>
      <ul class="service-list">
        <li class="wrap"><svg width="11" height="11" viewBox="0 0 11 11"><path d="M1 6l3 3 6-8" fill="none" stroke="currentColor" stroke-width="1.8"/></svg>Skilled Worker – Express Entry</li>
        <li class="wrap"><svg width="11" height="11" viewBox="0 0 11 11"><path d="M1 6l3 3 6-8" fill="none" stroke="currentColor" stroke-width="1.8"/></svg>SINP – Saskatchewan Immigration Nomination Program</li>
        <li><svg width="11" height="11" viewBox="0 0 11 11"><path d="M1 6l3 3 6-8" fill="none" stroke="currentColor" stroke-width="1.8"/></svg>Canadian Graduate Program</li>
        <li><svg width="11" height="11" viewBox="0 0 11 11"><path d="M1 6l3 3 6-8" fill="none" stroke="currentColor" stroke-width="1.8"/></svg>Hospitality</li>
        <li><svg width="11" height="11" viewBox="0 0 11 11"><path d="M1 6l3 3 6-8" fill="none" stroke="currentColor" stroke-width="1.8"/></svg>Federal Skilled Worker</li>
        <li><svg width="11" height="11" viewBox="0 0 11 11"><path d="M1 6l3 3 6-8" fill="none" stroke="currentColor" stroke-width="1.8"/></svg>Visitor Visa</li>
        <li><svg width="11" height="11" viewBox="0 0 11 11"><path d="M1 6l3 3 6-8" fill="none" stroke="currentColor" stroke-width="1.8"/></svg>Visitor Visa Extention</li>
        <li><svg width="11" height="11" viewBox="0 0 11 11"><path d="M1 6l3 3 6-8" fill="none" stroke="currentColor" stroke-width="1.8"/></svg>Student Category</li>
        <li><svg width="11" height="11" viewBox="0 0 11 11"><path d="M1 6l3 3 6-8" fill="none" stroke="currentColor" stroke-width="1.8"/></svg>Work Permit in Canada</li>
        <li><svg width="11" height="11" viewBox="0 0 11 11"><path d="M1 6l3 3 6-8" fill="none" stroke="currentColor" stroke-width="1.8"/></svg>Work Permit Outside Canada</li>
        <li><svg width="11" height="11" viewBox="0 0 11 11"><path d="M1 6l3 3 6-8" fill="none" stroke="currentColor" stroke-width="1.8"/></svg>Canadian Experience Class</li>
        <li><svg width="11" height="11" viewBox="0 0 11 11"><path d="M1 6l3 3 6-8" fill="none" stroke="currentColor" stroke-width="1.8"/></svg>Spousal Sponsorship</li>
      </ul>
    </div>
  </section>

  <section class="panel panel-contact">
    <div class="map-area" role="img" aria-label="Faint world map in the background"></div>
    <div class="brand brand-contact"><span class="brand-mark"></span>QRMT</div>
    <div class="sites">
      <p>www.qrmt.ca</p>
      <p>www.prairienominee.com</p>
      <p>www.northjobhub.ca</p>
    </div>
    <ul class="contact-list">
      <li><svg width="16" height="20" viewBox="0 0 16 20"><path d="M8 1a6 6 0 0 0-6 6c0 4.5 6 12 6 12s6-7.5 6-12a6 6 0 0 0-6-6z" fill="#fff"/><circle cx="8" cy="7" r="2.3" fill="var(--navy)"/></svg>#410-220 Maple Ave N.<br>Riverton, Saskatchewan<br>S4R-1K5</li>
      <li><svg width="22" height="14" viewBox="0 0 22 14"><path d="M1 6c4-6 16-6 20 0l-4 2-2-3H7L5 8z" fill="#fff"/><circle cx="11" cy="9" r="3.5" fill="#fff"/></svg>306-555-0142</li>
      <li><svg width="22" height="16" viewBox="0 0 22 16"><rect x="6" y="1" width="10" height="5" fill="#fff"/><rect x="1" y="6" width="20" height="9" rx="1.5" fill="#fff"/><rect x="5" y="9" width="12" height="2" fill="var(--navy)"/></svg>306-555-0187</li>
      <li><svg width="22" height="15" viewBox="0 0 22 15"><rect x="1" y="1" width="20" height="13" fill="#fff"/><path d="M1 1l10 8 10-8" fill="none" stroke="var(--navy)" stroke-width="1.5"/></svg>info@qrmt.ca</li>
    </ul>
  </section>

  <section class="panel panel-cover">
    <div class="brand brand-cover"><span class="brand-mark"></span>QRMT</div>
    <div class="cover-photo" role="img" aria-label="Photo of a diverse group of business people walking forward"></div>
    <p class="tagline">Take A Step With QRMT -<br>INTERNATIONAL IMMIGRATION &amp;<br>BUSINESS CONSULTING</p>
    <p class="slogan">...In the right Direction</p>
    <p class="cover-url">www.qrmt.ca</p>
  </section>

</main>
</body>
</html>
```